Creative Brief
Cedar Brook Emergency Center
Web Site
Health
www.CedarBrookER.example
We are the first Free Standing Emergency Room in Dallas! We have all the advantages of a hospital based ER without the hassle or wait. Add in customer service and a aesthetic environment and you will see what makes us so unique for you emergent medical needs.
Our free standing ER solution provides
No wait emergency rooms!
Open 24 hours a day, 7 days a week
State of the art equipment and diagnosing capabilities
All our doctors are trained Emergency Medicine physicians
Experienced friendly nurses
Onsite emergent radiology (x-rays, CAT scans, Ultrasound)
Onsite emergent laboratory with result within minutes
I like a clean website- not too busy. Needs to be professional. A few nice pictures representing emergency medicine. I do not want things that are overused like pictures of a heart or EKG strip. Please incorporate the logo and from the logo you can see they colors and fonts that I like
left side
I do not have any specific web sites that i like or dislike and am open to many options.
web content

```html
<!DOCTYPE html>
<html lang="en">
<head>
<meta charset="utf-8">
<title>Cedar Brook Emergency Center</title>
<link href="https://fonts.googleapis.com/css2?family=Oswald:wght@400;500&family=Arimo:wght@400;700&display=swap" rel="stylesheet">
<style>
  :root {
    --red: #b4181e;
    --red-dark: #8f1015;
    --slate: #3c4b56;
    --slate-dark: #2f3c45;
    --cream: #f5ecdc;
    --cream-edge: #e2d4bb;
    --page: #f4f1ea;
    --ink: #3a3a3a;
    --muted: #6b6b6b;
    --orange: #e7761c;
    --green: #6aa52a;
    --blue: #1f76b8;
    --white: #ffffff;
  }
  * { box-sizing: border-box; margin: 0; padding: 0; }
  html, body { width: 1200px; height: 1072px; overflow: hidden; }
  body {
    background: var(--page);
    font-family: "Arimo", Arial, sans-serif;
    color: var(--ink);
    position: relative;
  }
  .wrap { width: 813px; margin: 0 auto; position: relative; }

  /* Header */
  .site-header { height: 96px; background: var(--white); }
  .site-header .wrap { height: 96px; display: flex; justify-content: space-between; align-items: center; }
  .brand { font-family: "Oswald", sans-serif; font-weight: 500; color: var(--red); text-transform: uppercase; line-height: 1; }
  .brand-name { display: block; font-size: 40px; letter-spacing: 1px; }
  .brand-sub { display: block; font-size: 15px; letter-spacing: 6.5px; margin-top: 4px; }
  .contact { text-align: right; }
  .phone { font-family: "Oswald", sans-serif; font-size: 22px; color: var(--red); display: flex; align-items: center; justify-content: flex-end; gap: 6px; }
  .address { font-size: 11px; color: var(--muted); line-height: 1.35; margin-top: 2px; }

  /* Navigation */
  .main-nav { height: 38px; background: var(--slate); }
  .main-nav ul { list-style: none; display: flex; justify-content: space-between; align-items: center; height: 38px; padding: 0 18px 0 12px; }
  .main-nav a { font-family: "Oswald", sans-serif; font-size: 13px; color: var(--white); text-decoration: none; text-transform: uppercase; letter-spacing: .5px; padding: 4px 12px; border-radius: 3px; }
  .main-nav a.active { background: var(--red); }

  /* Hero */
  .hero { height: 331px; background: linear-gradient(180deg, var(--red) 0%, #c21f25 50%, var(--red-dark) 100%); padding-top: 20px; }
  .slider { position: relative; width: 828px; height: 288px; margin: 0 auto; background: var(--white); padding: 5px; box-shadow: 0 3px 10px rgba(0,0,0,.35); }
  .slide-photo { width: 100%; height: 100%; background: linear-gradient(90deg, #eef3f6 0%, #dfe9ef 40%, #c9dbe6 70%, #eef2f4 100%); position: relative; }
  .slide-caption { position: absolute; left: 14px; bottom: 20px; font-family: "Oswald", sans-serif; font-size: 19px; line-height: 1.2; color: #3b4650; text-transform: uppercase; }
  .slider-arrow { position: absolute; top: 127px; width: 34px; height: 34px; border-radius: 50%; background: var(--white); box-shadow: 0 1px 4px rgba(0,0,0,.4); display: flex; align-items: center; justify-content: center; }
  .slider-arrow.prev { left: -17px; }
  .slider-arrow.next { right: -17px; }

  /* Features */
  .features { display: flex; justify-content: space-between; margin-top: 20px; }
  .feature { width: 192px; height: 61px; border-radius: 4px; padding: 8px 10px; display: flex; justify-content: space-between; align-items: center; color: var(--white); font-family: "Oswald", sans-serif; font-size: 15px; line-height: 1.15; text-transform: uppercase; box-shadow: 0 2px 4px rgba(0,0,0,.2); }
  .feature.red { background: linear-gradient(180deg, #c8232a, var(--red-dark)); }
  .feature.orange { background: linear-gradient(180deg, #f08a2c, #d9650f); }
  .feature.green { background: linear-gradient(180deg, #7dbb37, #5a921f); }
  .feature.blue { background: linear-gradient(180deg, #2d89cd, #18629c); }

  /* Headings */
  .section-title { font-family: "Oswald", sans-serif; font-size: 20px; text-transform: uppercase; color: var(--ink); display: flex; align-items: center; gap: 8px; }
  .section-title em { font-style: normal; color: var(--red); }

  .welcome { margin-top: 24px; }
  .welcome p { font-size: 12px; line-height: 1.5; color: var(--muted); margin-top: 10px; }

  /* Panels */
  .panels { display: flex; justify-content: space-between; margin-top: 32px; }
  .panel { height: 261px; background: var(--cream); border: 1px solid var(--cream-edge); padding: 14px 12px; }
  .panel.services { width: 398px; }
  .panel.location { width: 392px; }
  .panel p { font-size: 11.5px; line-height: 1.45; color: var(--ink); margin-top: 10px; }
  .map { margin-top: 12px; height: 190px; background: linear-gradient(135deg, #efe6cf, #e4d9bd); border: 1px solid var(--cream-edge); }

  /* Footer */
  .site-footer { position: absolute; left: 0; right: 0; bottom: 0; height: 90px; background: var(--slate); border-top: 4px solid var(--slate-dark); }
  .site-footer .wrap { height: 86px; display: flex; justify-content: space-between; align-items: center; }
  .footer-links { font-size: 12px; color: var(--white); }
  .footer-links a { color: var(--white); text-decoration: none; }
  .copyright { font-size: 11px; color: #c9d1d6; margin-top: 8px; }
  .footer-brand { display: flex; align-items: center; gap: 10px; font-family: "Oswald", sans-serif; font-weight: 500; color: var(--white); text-transform: uppercase; font-size: 17px; line-height: 1.05; }
  .footer-brand .dot { width: 40px; height: 40px; border-radius: 50%; background: var(--slate-dark); border: 2px solid #54646f; }
</style>
</head>
<body>

<header class="site-header">
  <div class="wrap">
    <div class="brand">
      <span class="brand-name">Cedar Brook</span>
      <span class="brand-sub">Emergency Center</span>
    </div>
    <div class="contact">
      <div class="phone">
        <svg width="12" height="16" viewBox="0 0 12 16" aria-hidden="true"><path d="M2 1h3l1 4-2 1.5c.8 2 2 3.4 3.6 4.2L9 9l3 1.5V14c-6 1-11-5-10-13z" fill="#3c4b56"/></svg>
        +1.800.555.0142
      </div>
      <div class="address">4820 Alder Ave Suite<br>210, Dallas Texas 75219</div>
    </div>
  </div>
</header>

<nav class="main-nav">
  <ul class="wrap">
    <li><a class="active" href="#">Home</a></li>
    <li><a href="#">About Us</a></li>
    <li><a href="#">Services</a></li>
    <li><a href="#">For Providers</a></li>
    <li><a href="#">FAQs</a></li>
    <li><a href="#">Locations</a></li>
    <li><a href="#">Contact Us</a></li>
  </ul>
</nav>

<section class="hero">
  <div class="slider">
    <div class="slide-photo" role="img" aria-label="Photo of a smiling doctor with a stethoscope in front of a physician examining a patient">
      <div class="slide-caption">All our doctors are trained<br>emergency medicine physicians</div>
    </div>
    <span class="slider-arrow prev"><svg width="10" height="12" viewBox="0 0 10 12" aria-hidden="true"><path d="M8 1 2 6l6 5z" fill="#3c4b56"/></svg></span>
    <span class="slider-arrow next"><svg width="10" height="12" viewBox="0 0 10 12" aria-hidden="true"><path d="M2 1l6 5-6 5z" fill="#3c4b56"/></svg></span>
  </div>
</section>

<main class="wrap">
  <div class="features">
    <div class="feature red"><span>No wait emergency<br>rooms!</span><svg width="26" height="26" viewBox="0 0 26 26" aria-hidden="true"><circle cx="13" cy="13" r="12" fill="rgba(255,255,255,.25)"/><path d="M11 6h4v5h5v4h-5v5h-4v-5H6v-4h5z" fill="#fff"/></svg></div>
    <div class="feature orange"><span>Open 24 hours<br>7 days</span><svg width="26" height="26" viewBox="0 0 26 26" aria-hidden="true"><circle cx="13" cy="13" r="12" fill="rgba(255,255,255,.25)"/><path d="M11 6h4v5h5v4h-5v5h-4v-5H6v-4h5z" fill="#fff"/></svg></div>
    <div class="feature green"><span>Experienced<br>friendly nurses</span><svg width="26" height="26" viewBox="0 0 26 26" aria-hidden="true"><circle cx="13" cy="13" r="12" fill="rgba(255,255,255,.25)"/><path d="M11 6h4v5h5v4h-5v5h-4v-5H6v-4h5z" fill="#fff"/></svg></div>
    <div class="feature blue"><span>Onsite emergent<br>radiology / laboratory</span><svg width="26" height="26" viewBox="0 0 26 26" aria-hidden="true"><circle cx="13" cy="13" r="12" fill="rgba(255,255,255,.25)"/><path d="M11 6h4v5h5v4h-5v5h-4v-5H6v-4h5z" fill="#fff"/></svg></div>
  </div>

  <section class="welcome">
    <h2 class="section-title"><svg width="20" height="20" viewBox="0 0 20 20" aria-hidden="true"><circle cx="10" cy="10" r="9.5" fill="#b4181e"/><path d="M8.5 4.5h3v4h4v3h-4v4h-3v-4h-4v-3h4z" fill="#fff"/></svg><span>Welcome to <em>Cedar Brook Emergency Center</em></span></h2>
    <p>Cedar Brook Emergency Center offers hospital level emergency care without the long wait. Our board certified physicians, friendly nurses and onsite imaging and laboratory teams are here for you and your family every hour of every day of the year. Walk in any time and be seen by an emergency physician within minutes, with results explained clearly before you leave.</p>
  </section>

  <div class="panels">
    <section class="panel services">
      <h2 class="section-title"><svg width="20" height="20" viewBox="0 0 20 20" aria-hidden="true"><circle cx="10" cy="10" r="9.5" fill="#b4181e"/><path d="M8.5 4.5h3v4h4v3h-4v4h-3v-4h-4v-3h4z" fill="#fff"/></svg><span>Our <em>Services</em></span></h2>
      <p>Our free standing emergency room gives you all the advantages of a hospital based ER without the hassle. Every visit is handled by trained emergency medicine physicians.</p>
      <p>State of the art equipment lets us diagnose quickly. Onsite radiology covers x-rays, CAT scans and ultrasound, while our onsite laboratory returns most results within minutes so treatment can begin right away.</p>
      <p>Friendly nurses and staff make each visit calm, clear and comfortable for every patient.</p>
    </section>
    <section class="panel location">
      <h2 class="section-title"><svg width="20" height="20" viewBox="0 0 20 20" aria-hidden="true"><circle cx="10" cy="10" r="9.5" fill="#b4181e"/><path d="M8.5 4.5h3v4h4v3h-4v4h-3v-4h-4v-3h4z" fill="#fff"/></svg><span>Location <em>Map</em></span></h2>
      <div class="map" role="img" aria-label="Street map showing the emergency center location"></div>
    </section>
  </div>
</main>

<footer class="site-footer">
  <div class="wrap">
    <div>
      <div class="footer-links"><a href="#">Home</a> | <a href="#">About Us</a> | <a href="#">Services</a> | <a href="#">For Providers</a> | <a href="#">FAQs</a> | <a href="#">Sitemap</a> | <a href="#">Contact Us</a></div>
      <div class="copyright">Copy © 2011, Cedar Brook Emergency Center. All rights reserved.</div>
    </div>
    <div class="footer-brand"><span class="dot"></span><span>Cedar Brook<br>Emergency Center</span></div>
  </div>
</footer>

</body>
</html>
```